Flyer design for retail store owners

i would need to have a flyer design for my retail shop customers to show that I am a mailbox store that has all major shipping vendors to for their shipping needs. Ensuring that they can take advantage of opening a house account at the store and billed monthly, word document has all the details. Please use stock images for the notary public, passport photos, mailbox brass pictures of my actual mailboxes are listed in the pictures. I need to make it POP and WOW these retail store owners as I am using it to advertise the business

```html
<!DOCTYPE html>
<html lang="en">
<head>
<meta charset="utf-8">
<title>Mailbox Rental Flyer</title>
<link href="https://fonts.googleapis.com/css2?family=Roboto+Condensed:ital,wght@0,400;0,700;1,700&family=Roboto:wght@400&display=swap" rel="stylesheet">
<style>
  :root {
    --orange: #e8562a;
    --ink: #231f20;
    --text: #333333;
    --paper: #ffffff;
    --stage: #e9e9e9;
    --brass: #c9a36a;
    --brass-dark: #9c7a45;
  }
  * { margin: 0; padding: 0; box-sizing: border-box; }
  html, body { width: 1200px; height: 1200px; overflow: hidden; }
  body {
    background: var(--stage);
    font-family: "Roboto Condensed", "Arial Narrow", sans-serif;
    color: var(--text);
    position: relative;
  }
  .page {
    position: absolute;
    top: 238px;
    width: 560px;
    height: 724px;
    background: var(--paper);
    overflow: hidden;
    box-shadow: 0 6px 18px rgba(0,0,0,.18);
  }
  .page--front { left: 25px; }
  .page--back { left: 615px; }
  .abs { position: absolute; }
  .placeholder { position: absolute; border-radius: 2px; }

  /* front page */
  .hero-art {
    left: 36px; top: 32px; width: 256px; height: 250px;
    background: linear-gradient(135deg, #d9b98a 0%, var(--brass) 55%, var(--brass-dark) 100%);
  }
  .price-badge {
    left: 181px; top: 15px; width: 97px; height: 97px;
    border-radius: 50%;
    background: var(--orange);
    color: #fff;
    text-align: center;
    font-weight: 700;
    display: flex; flex-direction: column; justify-content: center;
    line-height: 1.15;
  }
  .price-badge__amount { font-size: 22px; }
  .price-badge__terms { font-size: 10px; }
  .hero-title { left: 326px; top: 72px; width: 226px; }
  .hero-title__kicker { color: var(--orange); font-weight: 700; font-size: 28px; line-height: 1; }
  .hero-title__main {
    color: var(--orange); font-weight: 700; font-size: 54px; line-height: .95;
    letter-spacing: -1.5px; white-space: nowrap;
  }
  .hero-title__body { font-size: 17.5px; line-height: 1.3; color: var(--ink); margin-top: 4px; }
  .hero-title__em { font-size: 23px; font-weight: 700; font-style: italic; color: var(--ink); margin-top: 2px; line-height: 1.2; }

  .intro-band {
    left: 0; top: 282px; width: 100%; height: 121px;
    background: var(--orange); color: #fff;
    padding: 14px 22px 0 38px;
    font-size: 11.6px; line-height: 1.35;
  }
  .intro-band p + p { margin-top: 14px; }
  .intro-band strong { font-weight: 700; }

  .promo { left: 38px; top: 418px; right: 18px; font-size: 11.6px; line-height: 1.36; color: var(--text); }
  .promo__heading { font-size: 17px; font-weight: 700; color: var(--ink); margin-bottom: 6px; }
  .promo__subhead { color: var(--orange); font-weight: 700; font-size: 12.5px; margin: 10px 0 5px; }
  .deal-list { list-style: none; }
  .deal-list li { position: relative; padding-left: 14px; }
  .deal-list li::before {
    content: ""; position: absolute; left: 0; top: 4px;
    width: 8px; height: 8px; border-radius: 50%; background: var(--orange);
  }

  .cta-bar {
    left: 0; bottom: 0; width: 100%; height: 60px;
    background: var(--ink);
    display: flex; align-items: center; padding-left: 38px; gap: 10px;
  }
  .cta-bar__text { color: #fff; font-size: 17px; font-weight: 700; font-style: italic; }
  .cta-bar__phone { color: var(--orange); font-size: 27px; font-weight: 700; font-style: italic; letter-spacing: .5px; }

  /* back page */
  .service-band { left: 0; top: 94px; width: 100%; height: 183px; background: var(--orange); }
  .photo-frame {
    left: 31px; top: 46px; width: 266px; height: 264px;
    background: #fff; padding: 18px;
    box-shadow: 0 2px 6px rgba(0,0,0,.35);
  }
  .photo-frame__photo {
    width: 100%; height: 100%;
    background: linear-gradient(135deg, #d8b884 0%, var(--brass) 50%, #7d5f33 100%);
  }
  .mailbox-art {
    left: 452px; top: 14px; width: 80px; height: 138px;
    background: linear-gradient(180deg, var(--orange) 0%, #c8431c 70%, #6a4a2a 100%);
    border-radius: 36px 36px 4px 4px;
  }
  .service-title { left: 318px; top: 108px; width: 232px; color: #fff; }
  .service-title__name { font-family: "Roboto", Arial, sans-serif; font-size: 32px; line-height: 1.32; font-weight: 400; white-space: nowrap; }
  .service-title__goal { font-size: 16px; font-weight: 700; line-height: 1.35; margin-top: 4px; }

  .parcel-art {
    left: 44px; top: 347px; width: 122px; height: 93px;
    background: linear-gradient(135deg, #d9a86a 0%, #f1d27a 100%);
  }
  .line-copy { font-size: 17px; line-height: 1.3; color: var(--ink); }
  .line-copy--ship { left: 189px; top: 345px; }
  .rule { position: absolute; height: 1.5px; background: var(--ink); }
  .rule--ship { left: 189px; top: 425px; right: 0; }
  .line-copy--track { left: 26px; top: 455px; }
  .rule--track { left: 26px; top: 532px; width: 390px; }
  .delivery-art {
    left: 363px; top: 433px; width: 178px; height: 97px;
    background: linear-gradient(135deg, #bfe0f2 0%, #f4c542 60%, var(--orange) 100%);
  }
  .ready-heading {
    left: 0; top: 541px; width: 100%; text-align: center;
    color: var(--orange); font-weight: 700; font-size: 19.5px;
  }
  .extras { left: 0; top: 574px; width: 100%; text-align: center; font-size: 12.6px; line-height: 1.4; color: var(--ink); }

  .partners {
    left: 29px; top: 627px; width: 504px; height: 46px;
    border: 1px solid #555;
  }
  .partners__label {
    position: absolute; left: 50%; top: -9px; transform: translateX(-50%);
    background: #fff; padding: 0 6px;
    font-size: 12.6px; color: var(--ink); white-space: nowrap;
  }
  .partners__list {
    position: absolute; left: 0; right: 0; top: 16px;
    display: flex; justify-content: center; gap: 18px;
    font-size: 16px; font-weight: 700; color: var(--ink);
  }
</style>
</head>
<body>

<section class="page page--front">
  <div class="placeholder hero-art" role="img" aria-label="Photo of brass mailbox wall with an orange mailbox illustration on a post"></div>
  <div class="abs price-badge">
    <span class="price-badge__amount">$12</span>
    <span class="price-badge__terms">a month<br>for 6-12 months<br>leases!</span>
  </div>
  <div class="abs hero-title">
    <div class="hero-title__kicker">RENTING A</div>
    <div class="hero-title__main">MAIL BOX</div>
    <div class="hero-title__body">is one of the most<br>efficient and cost saving<br>methods for receiving your</div>
    <div class="hero-title__em">mail and packages.</div>
  </div>

  <div class="abs intro-band">
    <p><strong>Instead of having to worry about private security, weather conditions, sorting, and deliveries; all you have to do is pick-up your mail from our secured facility each day except Sundays.</strong></p>
    <p>You will get a notification when mail arrives whether envelope or package, it will be scanned in daily which other mailbox stores do not offer! We offer onsite Notary Public with no appointments and onsite Passport Photos and can ship out same day.</p>
  </div>

  <div class="abs promo">
    <h2 class="promo__heading">MAIN PROMOTION:</h2>
    <p>Now renting mailboxes on Maple Ridge Commons Shopping Center. We are offering all Maple Ridge Commons shopping center owners/employees an exclusive promo deal! $12 a month for 6-12 months leases! You get a mailbox in the shop, a book of stamps(20 count), 3 notarizations by appointment, 100 copies of black and white, and 100 copies of color. Please see associate for sign up!</p>
    <h3 class="promo__subhead">Check out these other deals!</h3>
    <ul class="deal-list">
      <li>As a retail owner, you know how important it is to keep your customers coming back - you will get 20% discount for printing services.</li>
      <li>We duplicate keys for $2/each, our regular price charge is $4/each. Save up to 50%!</li>
      <li>Lamination is also discounted at 10% off.</li>
      <li>10% off retail supplies ... must be minimum of 10$</li>
      <li>For house accounts -a 5% discount will be deducted monthly of billing change to invoicing PLUS we're giving another 5% of the discount if you upgrade and sign up for mailbox. Great right?</li>
    </ul>
  </div>

  <div class="abs cta-bar">
    <span class="cta-bar__text">Take advantage of this limited time offer now!</span>
    <span class="cta-bar__phone">1234567890</span>
  </div>
</section>

<section class="page page--back">
  <div class="abs service-band"></div>
  <div class="abs photo-frame">
    <div class="photo-frame__photo" role="img" aria-label="Photo of a brass mailbox with its door open"></div>
  </div>
  <div class="placeholder mailbox-art" role="img" aria-label="Orange mailbox illustration on a wooden post"></div>
  <div class="abs service-title">
    <div class="service-title__name">At Swift<br>Parcel &amp; Post,</div>
    <div class="service-title__goal">our goal is to make your<br>shipping experience as<br>convenient as possible.</div>
  </div>

  <div class="placeholder parcel-art" role="img" aria-label="Photo of a cardboard box and padded envelopes"></div>
  <p class="abs line-copy line-copy--ship">Whether you are Shipping Packages,<br>Documents, or Packages,<br>we are here to help.</p>
  <div class="rule rule--ship"></div>

  <p class="abs line-copy line-copy--track">Whether you want to track your package<br>or estimate the price of your package,<br>it is easy for you.</p>
  <div class="placeholder delivery-art" role="img" aria-label="Illustration of a hand holding a phone with a map and a delivery van in a city"></div>
  <div class="rule rule--track"></div>

  <h2 class="abs ready-heading">WE ARE READY TO HANDLE ALL OF YOUR POSTAL SERVICES!</h2>
  <p class="abs extras">Get also the services you need;<br>printing, copying, and stop in to purchase postage or shipping materials.</p>

  <div class="abs partners">
    <span class="partners__label">SERVICE POINT PARTNERS ARE</span>
    <div class="partners__list">
      <span>NationPost</span>
      <span>Velox Freight</span>
      <span>Parcelway</span>
      <span>Courier Nord</span>
    </div>
  </div>
</section>

</body>
</html>
```